I need a business card/logo designed that obviously describes my business. We are a residential appraisal and home inspection company in Springfield, MO. We offer residential appraisals, home inspection, pest inspection and radon gas measurement. We have been in business for 18 years and hold state certified residential appraisal licenses and DRUMI certified home inspection licenses. I have a logo that I really like and will attach, but would be open to new suggestions. I like more modern designs than traditional and would like a two sided card with our services, licenses and qualifications on the back.

```html
<!DOCTYPE html>
<html lang="en">
<head>
<meta charset="utf-8">
<title>Larkvale Dwelling Review — Business Card</title>
<link href="https://fonts.googleapis.com/css2?family=Open+Sans:wght@400;600;700&display=swap" rel="stylesheet">
<style>
  :root {
    --bg: #e9e4dd;
    --brown-light: #b39a7e;
    --brown: #8a6d4f;
    --brown-dark: #5e4632;
    --orange: #f08a24;
    --orange-soft: #f7b25a;
    --white: #ffffff;
    --ink: #3a2a1c;
  }
  * { box-sizing: border-box; margin: 0; padding: 0; }
  html, body { width: 1200px; height: 913px; overflow: hidden; }
  body {
    background: var(--bg);
    font-family: "Open Sans", Arial, sans-serif;
    position: relative;
  }
  .card {
    position: absolute;
    width: 560px;
    height: 320px;
    border-radius: 4px;
    overflow: hidden;
    box-shadow: 0 10px 28px rgba(60, 40, 20, 0.25);
  }
  .card--front {
    left: 27px; top: 296px;
    background: linear-gradient(160deg, var(--brown-light) 0%, var(--brown) 55%, var(--brown-dark) 100%);
    color: var(--white);
  }
  .card--back {
    left: 613px; top: 296px;
    background: var(--white);
    color: var(--ink);
  }
  .band { position: absolute; left: 0; top: 0; width: 560px; height: 320px; }

  /* front */
  .holder { position: absolute; left: 40px; top: 70px; }
  .holder__marks { position: absolute; left: 0; top: 6px; display: flex; flex-direction: column; gap: 4px; }
  .holder__marks span { width: 12px; height: 12px; display: block; }
  .holder__marks .mark-white { background: var(--white); }
  .holder__marks .mark-orange { background: var(--orange); }
  .holder__name { margin-left: 24px; font-size: 21px; font-weight: 700; letter-spacing: 0.5px; line-height: 1.1; }
  .holder__role { margin-left: 24px; font-size: 11px; font-weight: 600; color: var(--orange); letter-spacing: 1px; }
  .address { position: absolute; left: 64px; top: 122px; font-size: 13px; line-height: 1.35; font-style: normal; }
  .contact { position: absolute; left: 44px; top: 180px; list-style: none; font-size: 13px; line-height: 1.4; }
  .contact li { display: flex; align-items: center; gap: 8px; }
  .contact svg { width: 12px; height: 12px; flex: none; }
  .badge {
    position: absolute; left: 318px; top: 70px;
    width: 30px; height: 30px; border-radius: 50%;
    background: #e2c98a; border: 2px solid var(--white);
  }
  .brand { position: absolute; display: flex; align-items: center; gap: 8px; font-weight: 700; }
  .brand__dot { width: 14px; height: 14px; background: var(--orange); flex: none; }
  .card--front .brand { left: 366px; top: 72px; width: 170px; font-size: 19px; line-height: 1.1; color: var(--white); }

  /* back */
  .card--back .brand { left: 40px; top: 100px; width: 220px; font-size: 24px; line-height: 1.1; color: var(--brown); }
  .services {
    position: absolute; right: 36px; top: 36px; list-style: none;
    text-align: right; font-size: 11.5px; line-height: 1.45; color: var(--ink); letter-spacing: 0.3px;
  }
  .services li { display: flex; justify-content: flex-end; align-items: center; gap: 8px; }
  .services li::after { content: ""; width: 7px; height: 7px; border-radius: 50%; background: var(--orange-soft); }
  .tagline {
    position: absolute; left: 40px; top: 196px; width: 330px;
    font-size: 10.5px; font-weight: 700; line-height: 1.35; color: var(--ink);
  }
</style>
</head>
<body>

<section class="card card--front" aria-label="Business card front">
  <svg class="band" viewBox="0 0 560 320" aria-hidden="true">
    <polygon points="0,302 560,250 560,320 0,320" fill="var(--white)"/>
    <polygon points="0,312 560,264 560,320 0,320" fill="var(--orange)"/>
    <polygon points="440,261 560,250 560,264 460,273" fill="var(--brown-dark)" opacity="0.3"/>
  </svg>

  <div class="badge" role="img" aria-label="Certification badge"></div>
  <div class="brand"><span class="brand__dot"></span><span>Larkvale Dwelling Review</span></div>

  <div class="holder">
    <div class="holder__marks"><span class="mark-white"></span><span class="mark-orange"></span></div>
    <div class="holder__name">DANA WHITFIELD</div>
    <div class="holder__role">OWNER</div>
  </div>

  <address class="address">
    Larkvale Dwelling Review 482<br>
    W Cedar Bend Road Suite C<br>
    Springfield, MO 65810
  </address>

  <ul class="contact">
    <li><svg viewBox="0 0 12 12"><path d="M2 1h2l1 3-1.5 1a7 7 0 0 0 3.5 3.5L8 7l3 1v2a1 1 0 0 1-1 1A9 9 0 0 1 1 2a1 1 0 0 1 1-1z" fill="var(--orange)"/></svg>417-555-0142</li>
    <li><svg viewBox="0 0 12 12"><rect x="3" y="0.5" width="6" height="11" rx="1.2" fill="var(--orange)"/><rect x="4.2" y="2" width="3.6" height="7" fill="var(--brown)"/></svg>417-555-0187</li>
    <li><svg viewBox="0 0 12 12"><rect x="0.5" y="2" width="11" height="8" rx="1" fill="none" stroke="var(--orange)" stroke-width="1.3"/><path d="M1 2.5l5 4 5-4" fill="none" stroke="var(--orange)" stroke-width="1.3"/></svg>info@larkvalereview.com</li>
    <li><svg viewBox="0 0 12 12"><circle cx="6" cy="6" r="5" fill="none" stroke="var(--orange)" stroke-width="1.3"/><path d="M1 6h10M6 1c-2.5 3-2.5 7 0 10M6 1c2.5 3 2.5 7 0 10" fill="none" stroke="var(--orange)" stroke-width="1"/></svg>www.larkvalereview.com</li>
  </ul>
</section>

<section class="card card--back" aria-label="Business card back">
  <svg class="band" viewBox="0 0 560 320" aria-hidden="true">
    <polygon points="0,300 560,252 560,268 0,316" fill="var(--brown)"/>
    <polygon points="0,300 200,283 200,299 0,316" fill="var(--brown-light)"/>
    <polygon points="320,320 560,246 560,320" fill="var(--orange)"/>
  </svg>

  <ul class="services">
    <li>APPRAISAL</li>
    <li>HOME INSPECTION</li>
    <li>TERMITE</li>
    <li>RADON</li>
    <li>WELL &amp; SEPTIC INSPECTION</li>
    <li>ENERGY AUDITS</li>
  </ul>

  <div class="brand"><span class="brand__dot"></span><span>Larkvale Dwelling Review</span></div>

  <p class="tagline">With years of experience behind us, we're prepared to tackle anything from a first time buyer's starter home or a seasoned buyer purchasing a luxurious dream home</p>
</section>

</body>
</html>
```